Business Card for a Jewellery Brand

Business card for an upscale jewellery brand. Attached is the brand logo and icon and color board. I am looking for two card versions: one for the founder and one is generic. The card should be elegant and convey upscale and premium feel. I am open to both square and rectangle card shapes.

Industry/Entity Type

Jewelry

Contact Information for Business Card

Two cards: (1) Sunila Perumbadi (Founder) (2) General
(1) Sunila Perumbadi card should have Name: Sunila Perumbadi, Title: Founder Email id: sunila@quelm.com.au. Phone no: +61412555307
(2) Generic card should have Email id: info@quelm.com.au. Phone no: +61431555962

Requirements
Must have
• Workmark
• ICON
• Phone no
• Email ID
• ABN: 48917205563 (Note: ABN is Business number in Australia)
• Website: www.quelm.com.au
• Instagram: quelm_jewellery
• Facebook: @quelmjewellery
Nice to have
• Tagline

```html
<!DOCTYPE html>
<html lang="en">
<head>
<meta charset="utf-8">
<title>QUELM Business Cards</title>
<link href="https://fonts.googleapis.com/css2?family=Questrial&display=swap" rel="stylesheet">
<style>
  :root {
    --backdrop: #0b0b0b;
    --blush: #e8948f;
    --blush-deep: #d57f7b;
    --blush-light: #f0aaa5;
    --ivory: #fbf8f5;
    --ivory-vein: #ece8e4;
    --ink: #4a4a4a;
    --white: #ffffff;
  }
  * { margin: 0; padding: 0; box-sizing: border-box; }
  html, body {
    width: 1200px;
    height: 1000px;
    overflow: hidden;
    background: var(--backdrop);
    font-family: "Questrial", "Century Gothic", sans-serif;
  }
  .canvas {
    position: relative;
    width: 1200px;
    height: 1000px;
    display: flex;
    align-items: center;
    justify-content: center;
    gap: 60px;
  }
  .card {
    position: relative;
    width: 510px;
    height: 300px;
    border-radius: 14px;
    overflow: hidden;
  }
  .card-marble {
    position: absolute;
    inset: 0;
  }

  /* Front: brand card */
  .card-front { background: var(--blush); color: var(--white); }
  .card-front .card-marble {
    background:
      radial-gradient(ellipse 40% 55% at 30% 40%, var(--blush-deep) 0%, transparent 70%),
      radial-gradient(ellipse 35% 45% at 72% 65%, var(--blush-deep) 0%, transparent 70%),
      radial-gradient(ellipse 30% 40% at 60% 20%, var(--blush-light) 0%, transparent 70%),
      var(--blush);
    opacity: 0.9;
  }
  .wordmark {
    position: absolute;
    top: 92px;
    left: 0;
    right: 0;
    text-align: center;
    font-size: 72px;
    letter-spacing: 34px;
    padding-left: 34px;
    color: var(--white);
  }
  .front-details {
    position: absolute;
    left: 28px;
    right: 28px;
    bottom: 24px;
    display: flex;
    justify-content: space-between;
    align-items: center;
    font-size: 13px;
    letter-spacing: 0.3px;
  }
  .social {
    display: flex;
    align-items: center;
    gap: 7px;
  }
  .social-dot {
    width: 11px;
    height: 11px;
    border-radius: 50%;
    background: var(--white);
  }

  /* Back: founder card */
  .card-back { background: var(--ivory); color: var(--ink); }
  .card-back .card-marble {
    background:
      radial-gradient(ellipse 40% 50% at 25% 55%, var(--ivory-vein) 0%, transparent 70%),
      radial-gradient(ellipse 35% 45% at 75% 35%, var(--ivory-vein) 0%, transparent 70%),
      var(--ivory);
  }
  .brand-name {
    position: absolute;
    top: 46px;
    left: 0;
    right: 0;
    text-align: center;
    font-size: 26px;
    letter-spacing: 10px;
    padding-left: 10px;
    color: var(--blush);
  }
  .person {
    position: absolute;
    top: 110px;
    left: 0;
    right: 0;
    text-align: center;
  }
  .person-name { font-size: 19px; }
  .person-title { font-size: 17px; margin-top: 2px; }
  .divider {
    position: absolute;
    top: 182px;
    left: 26px;
    right: 26px;
    height: 2px;
    background: var(--blush);
  }
  .contact-row {
    position: absolute;
    top: 206px;
    left: 26px;
    right: 26px;
    display: flex;
    justify-content: space-between;
    font-size: 14px;
  }
</style>
</head>
<body>
<main class="canvas">
  <section class="card card-front">
    <div class="card-marble" role="img" aria-label="Soft pink marble swirl texture"></div>
    <div class="wordmark">QUELM</div>
    <div class="front-details">
      <span class="abn">ABN: 48917205563</span>
      <span class="social"><span class="social-dot"></span>quelm_jewellery</span>
      <span class="social"><span class="social-dot"></span>@quelmjewellery</span>
    </div>
  </section>

  <section class="card card-back">
    <div class="card-marble" role="img" aria-label="Faint ivory marble swirl texture"></div>
    <div class="brand-name">QUELM</div>
    <div class="person">
      <div class="person-name">Sunila Perumbadi</div>
      <div class="person-title">Founder</div>
    </div>
    <div class="divider"></div>
    <div class="contact-row">
      <span class="phone">+61 41 25 55 307</span>
      <span class="website">www.quelm.com.au</span>
      <span class="email">sunila@quelm.com.au</span>
    </div>
  </section>
</main>
</body>
</html>
```